Bimvoro Power Point Presentation

We need our presentation designed. Our current presentation is inconsistent, too text heavy, and complicated. We want this to be clean, sleek, and impressive as our references attached are.

Our colors are blue, black, and white.
Our font is roboto.

```html
<!DOCTYPE html>
<html lang="en">
<head>
<meta charset="utf-8">
<title>Bimvoro Presentation</title>
<link href="https://fonts.googleapis.com/css2?family=Roboto:wght@300;400;500;700;900&display=swap" rel="stylesheet">
<style>
:root{
  --blue:#1a73e8;
  --blue-dark:#1560c9;
  --blue-soft:#dbe8fb;
  --ink:#1f1f1f;
  --grey:#6b6b6b;
  --page:#f4f4f4;
  --slide:#ffffff;
  --band:#efefef;
  --white:#ffffff;
}
*{margin:0;padding:0;box-sizing:border-box}
html,body{width:796px;height:1200px;overflow:hidden;background:var(--page);font-family:'Roboto',Arial,sans-serif;color:var(--ink)}
.sheet{position:relative;width:796px;height:1200px}
.slide{position:absolute;width:348px;height:196px;background:var(--slide);overflow:hidden;box-shadow:0 1px 3px rgba(0,0,0,.12)}
.col-l{left:40px}.col-r{left:409px}
.row1{top:66px}.row2{top:284px}.row3{top:506px}.row4{top:728px}.row5{top:958px}
.abs{position:absolute}
.footer-band{position:absolute;left:0;right:0;bottom:0;height:15px;background:var(--band)}
.copyright{position:absolute;left:5px;bottom:5px;font-size:3px;color:var(--grey)}
.brand{display:flex;align-items:center;gap:2px;font-weight:500;color:var(--blue)}
.brand-mark{display:inline-block;background:var(--blue)}
.footer-brand{position:absolute;right:5px;bottom:3px;font-size:6px}
.footer-brand .brand-mark{width:5px;height:5px}
.footer-brand .num{color:var(--ink);font-size:3.5px;margin-left:3px}
.heading{color:var(--blue);font-weight:500;font-size:7.5px;letter-spacing:.1px}
.sub{font-size:3.2px;color:var(--grey);text-transform:uppercase;line-height:1.9}
.center{text-align:center;left:0;right:0}
.photo{position:absolute}

/* slide 1 */
.cover-photo{right:0;top:0;width:200px;height:196px;background:linear-gradient(135deg,#b8c3c9,#5c6b72 55%,#2f3a40)}
.cover-blob{left:0;top:0;width:196px;height:196px}
.cover-brand{left:18px;top:60px;font-size:13px;color:var(--white)}
.cover-brand .brand-mark{width:11px;height:11px;background:var(--white)}
.cover-title{left:18px;top:84px;color:var(--white);font-size:13.5px;font-weight:700}
.cover-sub{left:18px;top:100px;color:var(--white);font-size:12px;font-weight:300}
.cover-btn{left:19px;top:124px;width:49px;height:12px;border:1px solid var(--white);border-radius:6px;color:var(--white);font-size:3.3px;display:flex;align-items:center;justify-content:center;font-weight:500}

/* slide 2 */
.buy-photo{right:0;top:0;width:180px;height:181px;background:linear-gradient(90deg,rgba(255,255,255,1) 0%,rgba(226,222,214,.9) 25%,#c9c0b2 60%,#a99b86)}
.buy-label{left:10px;font-size:5.5px;font-weight:500}
.icon-item{position:absolute;width:40px;margin-left:-20px;text-align:center;font-size:3.2px;color:var(--grey)}
.icon-item svg{display:block;margin:0 auto 2px;width:10px;height:10px}
.partner{position:absolute;top:155px;font-size:5.5px;font-weight:500;color:var(--ink)}

/* slide 3 */
.indoor-col{position:absolute;top:43px;height:136px;width:111px;background:var(--blue)}
.indoor-col h4{height:15px;background:var(--blue-dark);color:var(--white);font-size:5px;font-weight:500;display:flex;align-items:center;justify-content:center}
.ring{position:absolute;width:32px;height:32px;margin:-16px 0 0 -16px;border:1px solid var(--white);border-radius:50%;display:flex;align-items:center;justify-content:center}
.ring svg{width:11px;height:11px}
.ring-label{position:absolute;width:50px;margin-left:-25px;text-align:center;color:var(--white);font-size:3.8px;line-height:1.5}

/* slide 4 */
.stat{position:absolute;width:60px;margin-left:-30px;text-align:center}
.stat b{display:block;color:var(--blue);font-size:7.5px;font-weight:500}
.stat span{font-size:3px;color:var(--grey);text-transform:uppercase}
.map{top:130px;height:33px;background:linear-gradient(135deg,#e2e4e8,#c9ccd2);border-radius:3px}
.collage{right:0;top:0;width:152px;height:180px;background:linear-gradient(135deg,#3a4b66,#7b6a5a 40%,#2e5a4a 70%,#1c2230);clip-path:polygon(42% 0,100% 0,100% 100%,0 100%)}

/* slide 5 */
.pitch-bg{left:0;top:0}
.pitch-text{left:22px;top:38px;width:165px;color:var(--white);font-size:10px;font-weight:300;line-height:16px;white-space:nowrap}
.pitch-text b{font-weight:500}
.screen{left:194px;top:57px;width:140px;height:81px;background:#2c2c2c;padding:2px;box-shadow:0 3px 6px rgba(0,0,0,.35)}
.screen-inner{width:100%;height:100%;background:var(--blue);display:flex;align-items:center;justify-content:center}
.screen .brand{color:var(--white);font-size:11px}
.screen .brand-mark{width:9px;height:9px;background:var(--white)}

/* slide 6 */
.spec-label{top:40px;font-size:5px;font-weight:500}
.spec{position:absolute;font-size:4.6px;color:#444;display:flex;gap:5px;line-height:1.5}
.tick{color:var(--blue);font-weight:700;font-size:5px}
.beach{left:207px;top:69px;width:210px;height:210px;border-radius:50%;border:1.5px solid var(--blue);background:linear-gradient(180deg,#4f9ad8 0%,#a9d4ef 38%,#e9e2cf 52%,#d6c6a4 100%)}

/* slide 7 */
.shelter{left:0;top:0;width:157px;height:182px;background:linear-gradient(135deg,#6d7a84,#a9a08f 50%,#4a4e4f);clip-path:polygon(0 0,100% 0,86% 100%,0 100%)}
.poster{left:43px;top:32px;width:76px;height:119px;background:var(--white);display:flex;align-items:center;justify-content:center}
.poster .brand{font-size:10px}
.poster .brand-mark{width:8px;height:8px}
.take-title{left:176px;top:32px;font-size:8.5px;color:var(--blue);font-weight:500}
.take-rule{left:176px;top:45px;width:16px;height:1px;background:var(--blue)}
.take{position:absolute;left:179px;width:150px;font-size:4.4px;color:#555;line-height:1.7;display:flex;gap:4px}

/* slide 8 */
.logo-dot{position:absolute;width:38px;height:38px;margin:-19px 0 0 -19px;border-radius:50%;background:var(--white);box-shadow:0 0 5px rgba(26,115,232,.25);display:flex;align-items:center;justify-content:center;font-size:4.8px;font-weight:500;color:var(--ink);text-align:center}

/* slide 9 */
.thanks{background:var(--blue)}
.thanks-mark{left:145px;top:44px;width:58px;height:48px;background:var(--white);border-radius:6px}
.thanks-name{top:97px;color:var(--white);font-size:7px;font-weight:500}
.thanks-title{top:108px;color:var(--white);font-size:36px;font-weight:700;letter-spacing:.5px}
.thanks .copyright,.thanks .page{color:rgba(255,255,255,.8)}
.page{position:absolute;right:5px;bottom:5px;font-size:3px}
</style>
</head>
<body>
<div class="sheet">

  <!-- Cover -->
  <section class="slide col-l row1">
    <div class="photo cover-photo" role="img" aria-label="Photo of a person viewing a digital screen in an indoor hall"></div>
    <svg class="abs cover-blob" viewBox="0 0 196 196"><path d="M0 0H80C120 10 190 70 194 110C196 150 150 180 90 196H0Z" fill="#1a73e8"/></svg>
    <div class="abs brand cover-brand"><span class="brand-mark"></span>Bimvoro</div>
    <div class="abs cover-title">Indoor DOOH</div>
    <div class="abs cover-sub">Audiences at Scale</div>
    <div class="abs cover-btn">BUY ON BIMVORO</div>
  </section>

  <!-- How to buy -->
  <section class="slide col-r row1">
    <div class="photo buy-photo" role="img" aria-label="Photo of a sidewalk sign stand with a screen at a seaside cafe"></div>
    <div class="abs heading" style="left:10px;top:19px">HOW TO BUY</div>
    <div class="abs sub" style="left:10px;top:30px">Bimvoro's network and unique audiences are accessible however you buy your media.</div>
    <div class="abs buy-label" style="top:49px">AUDIENCES...</div>
    <div class="icon-item" style="left:22px;top:64px"><svg viewBox="0 0 10 10"><circle cx="5" cy="5" r="4" fill="none" stroke="#1a73e8" stroke-width=".8"/></svg>High net worth</div>
    <div class="icon-item" style="left:70px;top:64px"><svg viewBox="0 0 10 10"><rect x="1" y="2" width="8" height="6" fill="none" stroke="#1a73e8" stroke-width=".8"/><line x1="5" y1="2" x2="5" y2="8" stroke="#1a73e8" stroke-width=".6"/></svg>Sports Fans</div>
    <div class="icon-item" style="left:114px;top:64px"><svg viewBox="0 0 10 10"><circle cx="5" cy="5" r="4" fill="none" stroke="#1a73e8" stroke-width=".8"/><path d="M5 3V5H7" stroke="#1a73e8" stroke-width=".7" fill="none"/></svg>High dwell time</div>
    <div class="icon-item" style="left:158px;top:64px"><svg viewBox="0 0 10 10"><circle cx="5" cy="5" r="3" fill="none" stroke="#1a73e8" stroke-width=".8"/><circle cx="5" cy="5" r="1" fill="#1a73e8"/></svg>And many more.</div>
    <div class="abs buy-label" style="top:95px">HOWEVER YOU'D LIKE.</div>
    <div class="icon-item" style="left:22px;top:110px"><svg viewBox="0 0 10 10"><path d="M2 8L5 2L8 8Z" fill="none" stroke="#1a73e8" stroke-width=".8"/></svg>Direct Buying</div>
    <div class="icon-item" style="left:70px;top:110px"><svg viewBox="0 0 10 10"><circle cx="2" cy="2" r="1" fill="#1a73e8"/><circle cx="8" cy="2" r="1" fill="#1a73e8"/><circle cx="5" cy="8" r="1" fill="#1a73e8"/><path d="M2 2L5 8L8 2" stroke="#1a73e8" stroke-width=".6" fill="none"/></svg>Open RTB</div>
    <div class="icon-item" style="left:114px;top:110px"><svg viewBox="0 0 10 10"><rect x="1.5" y="1.5" width="7" height="7" fill="none" stroke="#1a73e8" stroke-width=".8"/></svg>Programmatic<br>Guaranteed or PMP</div>
    <div class="abs buy-label" style="top:140px">YOU CAN BUY ANYWHERE...</div>
    <div class="partner" style="left:10px">Quillmetric</div>
    <div class="partner" style="left:45px;font-size:4.5px">TradeHarbor</div>
    <div class="partner" style="left:83px">Zentio</div>
    <div class="partner" style="left:128px">Roamly</div>
    <div class="partner" style="left:170px">Veltra</div>
    <div class="footer-band"></div>
    <div class="copyright">© Copyright 2021 Bimvoro. All Rights Reserved.</div>
    <div class="brand footer-brand"><span class="brand-mark"></span>Bimvoro<span class="num">02</span></div>
  </section>

  <!-- Why go indoor -->
  <section class="slide col-l row2">
    <div class="abs heading center" style="top:12px;text-align:center">WHY GO INDOOR</div>
    <div class="abs sub center" style="top:21px;text-align:center">It's not just lockdowns ending – recent uptick has been driven by the unique<br>effectiveness of indoor DOOH ad exposure.</div>
    <div class="indoor-col" style="left:5px"><h4>IT'S SPECIAL</h4></div>
    <div class="indoor-col" style="left:118px"><h4>IT'S POWERFUL</h4></div>
    <div class="indoor-col" style="left:231px"><h4>AND IT WORKS</h4></div>
    <div class="ring" style="left:33px;top:83px"><svg viewBox="0 0 12 12"><ellipse cx="6" cy="6" rx="5" ry="3" fill="none" stroke="#fff" stroke-width="1"/><circle cx="6" cy="6" r="1.5" fill="#fff"/></svg></div>
    <div class="ring-label" style="left:33px;top:101px">Dwell time measured in minutes, not seconds</div>
    <div class="ring" style="left:88px;top:83px"><svg viewBox="0 0 12 12"><circle cx="6" cy="6" r="5" fill="none" stroke="#fff" stroke-width="1.4"/><circle cx="6" cy="6" r="2" fill="none" stroke="#fff" stroke-width="1"/></svg></div>
    <div class="ring-label" style="left:88px;top:101px">Brand-safe</div>
    <div class="ring" style="left:33px;top:141px"><svg viewBox="0 0 12 12"><circle cx="6" cy="3.5" r="2.3" fill="#fff"/><path d="M2 11C2 7 10 7 10 11Z" fill="#fff"/></svg></div>
    <div class="ring-label" style="left:33px;top:159px">100% viewability by humans, not bots</div>
    <div class="ring" style="left:88px;top:141px"><svg viewBox="0 0 12 12"><path d="M1 6L11 1L8 11L6 7Z" fill="none" stroke="#fff" stroke-width="1"/></svg></div>
    <div class="ring-label" style="left:88px;top:159px">Not Skippable</div>
    <div class="ring" style="left:147px;top:83px"><svg viewBox="0 0 12 12"><path d="M1 4H4L9 1V11L4 8H1Z" fill="#fff"/></svg></div>
    <div class="ring-label" style="left:147px;top:101px">Engaged impressions, consumer attention, means...</div>
    <div class="ring" style="left:203px;top:83px"><svg viewBox="0 0 12 12"><circle cx="6" cy="6" r="5" fill="none" stroke="#fff" stroke-width="1"/><circle cx="6" cy="6" r="2.5" fill="none" stroke="#fff" stroke-width="1"/><circle cx="6" cy="6" r="1" fill="#fff"/></svg></div>
    <div class="ring-label" style="left:203px;top:101px">...Indoor DOOH 2x more likely to be seen, recalled, than traditional OOH</div>
    <div class="ring" style="left:286px;top:83px"><svg viewBox="0 0 12 12"><rect x="4.5" y="1" width="3" height="3" fill="#fff"/><rect x="1" y="8" width="3" height="3" fill="#fff"/><rect x="4.5" y="8" width="3" height="3" fill="#fff"/><rect x="8" y="8" width="3" height="3" fill="#fff"/><path d="M6 4V8M2.5 8V6H9.5V8" stroke="#fff" stroke-width=".7" fill="none"/></svg></div>
    <div class="ring-label" style="left:286px;top:101px;width:60px;margin-left:-30px">2x increase in reach if added to Omni-Channel campaigns</div>
    <div class="footer-band"></div>
    <div class="copyright">© Copyright 2021 Bimvoro. All Rights Reserved.</div>
    <div class="brand footer-brand"><span class="brand-mark"></span>Bimvoro<span class="num">02</span></div>
  </section>

  <!-- Network -->
  <section class="slide col-r row2">
    <div class="photo collage" role="img" aria-label="Collage of many venue and travel photographs in a receding wall of screens"></div>
    <div class="abs heading" style="left:12px;top:19px">NETWORK</div>
    <div class="abs sub" style="left:12px;top:29px">Bimvoro is your DOOH partner, connecting your partners and advertisers<br>to a nation-wide network of premium, place-based screens.</div>
    <div class="stat" style="left:36px;top:59px"><b>12B+</b><span>Impressions annually</span></div>
    <div class="stat" style="left:94px;top:59px"><b>26,105+</b><span>Venues</span></div>
    <div class="stat" style="left:148px;top:59px"><b>31,594+</b><span>Screens</span></div>
    <div class="stat" style="left:36px;top:96px"><b>12000+</b><span>Retail screens</span></div>
    <div class="stat" style="left:94px;top:96px"><b>16000+</b><span>Restobar screens</span></div>
    <div class="stat" style="left:148px;top:96px"><b>2000+</b><span>Medical screens</span></div>
    <div class="abs map" style="left:17px;width:66px" role="img" aria-label="Map of United States venue locations"></div>
    <div class="abs map" style="left:101px;width:58px" role="img" aria-label="Map of Canada venue locations"></div>
    <div class="footer-band"></div>
    <div class="copyright">© Copyright 2021 Bimvoro. All Rights Reserved.</div>
    <div class="brand footer-brand"><span class="brand-mark"></span>Bimvoro<span class="num">02</span></div>
  </section>

  <!-- Pitch -->
  <section class="slide col-l row3">
    <svg class="abs pitch-bg" width="348" height="181" viewBox="0 0 348 181"><path d="M0 0H213C185 40 168 90 177 120C183 145 192 165 199 181H0Z" fill="#1a73e8"/></svg>
    <p class="abs pitch-text">Bimvoro offers advertisers<br>easy, affordable access to<br><b>North America's largest</b><br><b>indoor DOOH network,</b><br>containing <b>diverse audience</b><br><b>segments</b> while <b>captivated</b><br><b>in indoor environments</b></p>
    <div class="abs screen"><div class="screen-inner"><div class="brand"><span class="brand-mark"></span>Bimvoro</div></div></div>
    <div class="footer-band"></div>
    <div class="copyright">© Copyright 2021 Bimvoro. All Rights Reserved.</div>
    <div class="brand footer-brand"><span class="brand-mark"></span>Bimvoro<span class="num">03</span></div>
  </section>

  <!-- Formats -->
  <section class="slide col-r row3">
    <div class="abs beach" role="img" aria-label="Photo of a sunny beach with palm trees and a surf sign"></div>
    <div class="abs heading center" style="top:12px;text-align:center">DIGITAL MEDIA FORMATS</div>
    <div class="abs sub center" style="top:22px;text-align:center">Specifications</div>
    <div class="abs spec-label" style="left:9px">NETWORK</div>
    <div class="abs spec-label" style="left:102px">CONTENT SPECIFICATIONS</div>
    <div class="spec" style="left:9px;top:55px"><span class="tick">✓</span>Indoor, 32 –73" Screens</div>
    <div class="spec" style="left:9px;top:71px"><span class="tick">✓</span>Full Screen Take Over</div>
    <div class="spec" style="left:9px;top:88px"><span class="tick">✓</span>Sold programmatically</div>
    <div class="spec" style="left:9px;top:107px"><span class="tick">✓</span>No Blacklisted Advertisers</div>
    <div class="spec" style="left:9px;top:125px"><span class="tick">✓</span>Approval Upon Venue Review</div>
    <div class="spec" style="left:102px;top:55px"><span class="tick">✓</span>1920 pixels (w) x 1080 pixels (h) 16:9</div>
    <div class="spec" style="left:102px;top:71px"><span class="tick">✓</span>1080 pixels (w) x 1920 pixels (h) 9:16</div>
    <div class="spec" style="left:102px;top:88px"><span class="tick">✓</span>Static: PNG, RGB, encoded .JPG or H.264</div>
    <div class="spec" style="left:102px;top:107px"><span class="tick">✓</span>Video: .MP5 / encoded .MOV</div>
    <div class="spec" style="left:102px;top:125px"><span class="tick">✓</span><span>Will repurpose TV spots, banner ads,<br>transcode ill-fitting static creatives</span></div>
    <div class="footer-band"></div>
    <div class="copyright">© Copyright 2021 Bimvoro. All Rights Reserved.</div>
    <div class="brand footer-brand"><span class="brand-mark"></span>Bimvoro<span class="num">03</span></div>
  </section>

  <!-- Takeaways -->
  <section class="slide col-l row4">
    <div class="photo shelter" role="img" aria-label="Photo of a city bus shelter with a backlit poster"></div>
    <div class="abs poster"><div class="brand"><span class="brand-mark"></span>Bimvoro</div></div>
    <div class="abs take-title">BIMVORO | KEY TAKEAWAYS</div>
    <div class="abs take-rule"></div>
    <div class="take" style="top:57px"><span class="tick">✓</span><span>North America's largest and fastest-growing indoor DOOH screen network</span></div>
    <div class="take" style="top:81px"><span class="tick">✓</span><span>Powerful enough to capture the attention of nationwide audiences at scale, specific enough to provide access to diverse audience segments</span></div>
    <div class="take" style="top:111px"><span class="tick">✓</span><span>Programmatically-accessible, ensuring cost-efficiency, transparency and real-time optimizations</span></div>
    <div class="take" style="top:137px"><span class="tick">✓</span><span>Flexible enough to get any DOOH campaign or integration up and running quickly and without issue</span></div>
    <div class="footer-band"></div>
    <div class="copyright">© Copyright 2021 Bimvoro. All Rights Reserved.</div>
    <div class="brand footer-brand"><span class="brand-mark"></span>Bimvoro<span class="num">04</span></div>
  </section>

  <!-- Advertisers -->
  <section class="slide col-r row4" style="left:411px">
    <div class="abs heading center" style="top:14px;text-align:center">ADVERTISERS</div>
    <div class="abs sub center" style="top:23px;text-align:center">Brands that buy on our network</div>
    <div class="logo-dot" style="left:41px;top:58px">Norvik</div>
    <div class="logo-dot" style="left:108px;top:58px">Lirae</div>
    <div class="logo-dot" style="left:175px;top:58px">Starbloom</div>
    <div class="logo-dot" style="left:242px;top:58px">Dashvale</div>
    <div class="logo-dot" style="left:308px;top:58px">Ardent</div>
    <div class="logo-dot" style="left:75px;top:104px">Northland</div>
    <div class="logo-dot" style="left:142px;top:104px">Hemkoll</div>
    <div class="logo-dot" style="left:209px;top:104px">Dotties</div>
    <div class="logo-dot" style="left:276px;top:104px">Paycircle</div>
    <div class="logo-dot" style="left:41px;top:150px">Golden Bun</div>
    <div class="logo-dot" style="left:108px;top:150px">Puckline</div>
    <div class="logo-dot" style="left:175px;top:150px">Pixora</div>
    <div class="logo-dot" style="left:242px;top:150px">Tessaro</div>
    <div class="logo-dot" style="left:308px;top:150px">Tunely</div>
    <div class="footer-band"></div>
    <div class="copyright">© Copyright 2021 Bimvoro. All Rights Reserved.</div>
    <div class="brand footer-brand"><span class="brand-mark"></span>Bimvoro<span class="num">05</span></div>
  </section>

  <!-- Thank you -->
  <section class="slide col-l row5 thanks">
    <div class="abs thanks-mark"></div>
    <div class="abs thanks-name center" style="text-align:center">Bimvoro</div>
    <div class="abs thanks-title center" style="text-align:center">THANK YOU</div>
    <div class="copyright">© Copyright 2021 Bimvoro. All Rights Reserved.</div>
    <div class="page">Page 06</div>
  </section>

</div>
</body>
</html>
```